Body corporate management needs business principle flyer design

We need a one page A4 flyer design for our business principles.
We manage body corporates and strata properties.
Brightwick is a new initiative for our company. Its a label that we have given to our principles of business that drive our people, systems and processes to give assurance to our clients that every detail matters.
We would like to be able to include this design in future brochure so we are after 1 x portrait and 1 x landscape.
The design needs to portray professionalism.
We would like to see designs that use the colour red. (see attached logo).

Target Market(s)

Professionals

Industry/Entity Type

Business

Font styles to use
Sans Serif

Requirements
Must have
• Brightwick logo, provide the design file and as pdf
Nice to have
• the use of the colour red from the logo

```html
<!DOCTYPE html>
<html lang="en">
<head>
<meta charset="utf-8">
<title>Brightwick – Principles of Business</title>
<link rel="stylesheet" href="https://fonts.googleapis.com/css2?family=Roboto+Condensed:wght@300;400;700&display=swap">
<style>
  :root {
    --red: #e63a2e;
    --ink: #1f1f1f;
    --black: #000000;
    --paper: #ffffff;
    --white: #ffffff;
    --line: 24px;
  }
  * { margin: 0; padding: 0; box-sizing: border-box; }
  html, body { width: 849px; height: 1200px; overflow: hidden; background: var(--paper); }
  .flyer {
    position: relative;
    width: 849px;
    height: 1200px;
    overflow: hidden;
    font-family: "Roboto Condensed", "Arial Narrow", sans-serif;
    color: var(--ink);
  }
  .disc { position: absolute; left: 0; top: 0; }
  .brand {
    position: absolute;
    left: 38px;
    top: 506px;
    font-weight: 300;
    font-size: 58px;
    line-height: 1;
    color: var(--red);
    letter-spacing: 0.5px;
  }
  .brand-statement {
    position: absolute;
    left: 40px;
    top: 582px;
    color: var(--white);
    font-size: 17px;
    line-height: 41px;
  }
  .principle {
    position: absolute;
    left: 0;
    width: 849px;
    font-size: 15px;
    line-height: var(--line);
  }
  .principle-title {
    color: var(--red);
    font-weight: 700;
    font-size: 17px;
    margin-left: var(--x);
  }
  .principle-line { margin-left: var(--x); white-space: nowrap; }
</style>
</head>
<body>
<main class="flyer">
  <svg class="disc" width="849" height="1200" viewBox="0 0 849 1200" aria-hidden="true">
    <circle cx="-83" cy="596" r="434" fill="var(--black)" stroke="var(--red)" stroke-width="5"/>
  </svg>

  <div class="brand">Brightwick</div>
  <p class="brand-statement">
    Brightwick is our principles of business<br>
    that drive our people, systems and<br>
    processes to give assurance to our<br>
    clients that every detail matters.
  </p>

  <section class="principle" style="top:41px">
    <h2 class="principle-title" style="--x:66px">Client Experience</h2>
    <p class="principle-line" style="--x:66px">Our promise is to pursue excellence and to continually deliver a solutions based service. We achieve this through</p>
    <p class="principle-line" style="--x:66px">active engagement, open channels of communication and a serviced led team with the dedicated resources to listen,</p>
    <p class="principle-line" style="--x:66px">engage and implement.</p>
  </section>

  <section class="principle" style="top:136px">
    <h2 class="principle-title" style="--x:114px">Loyalty</h2>
    <p class="principle-line" style="--x:168px">We seek to develop a life-time relationship with our clients, building trust by acting with integrity,</p>
    <p class="principle-line" style="--x:204px">honesty and courtesy. We achieve this due to our expert approach to strata management and</p>
    <p class="principle-line" style="--x:236px">providing a responsive service to our clients.</p>
  </section>

  <section class="principle" style="top:232px">
    <h2 class="principle-title" style="--x:269px">Education and Guidance</h2>
    <p class="principle-line" style="--x:288px">We endeavor to always be proactive in client education and guidance. This is</p>
    <p class="principle-line" style="--x:308px">achieved by our internal and external communications, comprehensive training</p>
    <p class="principle-line" style="--x:326px">programs and cross-departmental collaboration of knowledge sharing.</p>
  </section>

  <section class="principle" style="top:329px">
    <h2 class="principle-title" style="--x:343px">Compliance and Governance</h2>
    <p class="principle-line" style="--x:355px">We engage and own a position of ‘every detail matters’. We give due</p>
    <p class="principle-line" style="--x:366px">diligence to the relevant state and national legislations with which</p>
    <p class="principle-line" style="--x:374px">we, our clients and our stakeholders must comply. We regulate and</p>
    <p class="principle-line" style="--x:380px">achieve this through a robust system of internal processes and</p>
    <p class="principle-line" style="--x:388px">protocols which structure and confirm our deliverables are in line</p>
    <p class="principle-line" style="--x:396px">with regulations.</p>
  </section>

  <section class="principle" style="top:493px">
    <h2 class="principle-title" style="--x:401px">Systems and processes</h2>
    <p class="principle-line" style="--x:406px">We strive to be the best in our field, by implementing</p>
    <p class="principle-line" style="--x:408px">efficiencies without compromising service quality, accuracy or</p>
    <p class="principle-line" style="--x:408px">compliance. We continually seek to achieve this by reviewing,</p>
    <p class="principle-line" style="--x:408px">updating and adopting continuous improvement strategies,</p>
    <p class="principle-line" style="--x:408px">systems and quality processes that deliver outcomes.</p>
  </section>

  <section class="principle" style="top:636px">
    <h2 class="principle-title" style="--x:407px">Quality and Commitment</h2>
    <p class="principle-line" style="--x:403px">We invest in the recruitment and retention of a quality and</p>
    <p class="principle-line" style="--x:398px">diverse team of experienced professionals with a strong focus</p>
    <p class="principle-line" style="--x:392px">on continual professional development.&nbsp; As committed and</p>
    <p class="principle-line" style="--x:386px">skilled individuals, we actively promote the cross-departmental</p>
    <p class="principle-line" style="--x:386px">collaboration with one another to deliver a well rounded offering.</p>
  </section>

  <section class="principle" style="top:777px">
    <h2 class="principle-title" style="--x:379px">Delivery</h2>
    <p class="principle-line" style="--x:371px">We empower our teams to deliver an outstanding client service and</p>
    <p class="principle-line" style="--x:364px">to be accountable for their actions. We will make sure every detail</p>
    <p class="principle-line" style="--x:352px">matters, provide valuable insight and supply information in a clear and</p>
    <p class="principle-line" style="--x:352px">timely manner.</p>
  </section>

  <section class="principle" style="top:897px">
    <h2 class="principle-title" style="--x:317px">Integrity</h2>
    <p class="principle-line" style="--x:298px">Our approach to strata management is bound by honesty and a strong set</p>
    <p class="principle-line" style="--x:276px">of moral principles. We act in our clients’ best interests with diligence and</p>
    <p class="principle-line" style="--x:252px">transparency for understanding and accountability.</p>
  </section>

  <section class="principle" style="top:993px">
    <h2 class="principle-title" style="--x:222px">Continuous Improvement</h2>
    <p class="principle-line" style="--x:186px">Our goal is to continually evolve to better our offering and to be adaptable and responsive to</p>
    <p class="principle-line" style="--x:142px">change. Our infrastructure supports us to continually mould into the business that is right for our clients.</p>
  </section>

  <section class="principle" style="top:1064px">
    <h2 class="principle-title" style="--x:66px">Ethical Stance</h2>
    <p class="principle-line" style="--x:66px">We aim to create a community of ethical business relationships where we contribute our values and services to give</p>
    <p class="principle-line" style="--x:66px">our clients outstanding reassurance of our abilities.</p>
  </section>
</main>
</body>
</html>
```